Pellinex header in combination with existing logo

The header of the Pellinex profile% 26quot; https: //www.pellinex.com/company/morvadaconsulting%26quot; shall be renewed. Therefore, a new background image shall be designed. A design is simple, clear, well structured and fits the consulting business. This article should be used as a separate project for publications. It will become the corporate identity for social media and employer branding. In case you have any questions, feel free to contact us.b ***************** * Background *: MORVADA is a leading international management consultancy for operations. With unique concepts and the right employees, we achieve effective results. We support well-known companies from industry and trade in the optimization of the total value-added chain all over the world. Our custom-tailored approach enables us to quickly optimize our customer's processes along the value-added chain. Morvada works in the following branches: - Automotive / Automotive supplier - Pharmaceutical - Foundry - Shipyard - Steel industry - Consumer goods - Energy - Engineering - Electronics - Facility engineering% 26amp; construction

Target Market(s)

Consulting / Industry (Pharmaceutical, productive industry, metal, shipbuilding, automotive)

Industry/Entity Type

Management Consulting

Font styles to use
Other font styles liked:
• see PPT

Colors

Designer to choose colors to be used in the design.

Requirements
Must have
• Please follow the recommended Pellinex resolution guideline (see also: Pellinex_Guideline.jpg). Rectangular background (see page 26) kelm_award_list% 26quot; kelm_award_list% 26quot;, three sizes next to each other) right.
Nice to have
• PowerPoint presentation as a guideline however, not as a must have in case you want to use images. You want to find various available licensed pictures. These can be used, but we believe that a simple and neutral (abstract?) Background image would be better. - 26gt%; You are also considered if you do not use one of the provided pictures at all! We want to test a simplistic design as well. Convince us!

```html
<!DOCTYPE html>
<html lang="en">
<head>
<meta charset="utf-8">
<title>Morvada Management Consulting – Pellinex header</title>
<link rel="stylesheet" href="https://fonts.googleapis.com/css2?family=Hind:wght@400;600&display=swap">
<style>
  :root {
    --page: #ffffff;
    --ink-grey: #5b646c;
    --panel: #e4e5e9;
    --navy: #141a33;
    --steel: #3b4260;
    --haze: #cfd4de;
    --table: #d9dde4;
    --gold-light: #d9b866;
    --gold-mid: #b48a3a;
    --gold-dark: #8c6721;
    --badge-white: #fbfbfb;
    --badge-edge: #d6d6d6;
  }
  html, body {
    margin: 0;
    padding: 0;
    width: 1200px;
    height: 1200px;
    overflow: hidden;
    background: var(--page);
  }
  .canvas {
    position: relative;
    width: 1200px;
    height: 1200px;
    background: var(--page);
  }
  .header-banner {
    position: absolute;
    left: 50px;
    top: 464px;
    width: 1099px;
    height: 272px;
  }
  .header-photo {
    position: absolute;
    left: 0;
    top: 0;
    width: 957px;
    height: 272px;
    background:
      radial-gradient(ellipse 55% 22% at 30% 100%, rgba(217,221,228,0.55) 0%, rgba(217,221,228,0) 100%),
      linear-gradient(90deg, var(--haze) 0%, #9aa0b4 10%, #5d6584 26%, var(--steel) 42%, #262d49 62%, var(--navy) 100%);
  }
  .brand-panel {
    position: absolute;
    left: 602px;
    top: 0;
    width: 355px;
    height: 67px;
  }
  .brand-panel svg {
    position: absolute;
    inset: 0;
  }
  .brand-name {
    position: absolute;
    left: 86px;
    top: 5px;
    margin: 0;
    font-family: "Hind", sans-serif;
    font-weight: 600;
    font-size: 40px;
    letter-spacing: 2px;
    line-height: 1;
    color: var(--ink-grey);
  }
  .brand-tagline {
    position: absolute;
    right: 8px;
    top: 44px;
    margin: 0;
    font-family: "Hind", sans-serif;
    font-weight: 400;
    font-size: 17px;
    letter-spacing: 0.3px;
    line-height: 1;
    color: var(--ink-grey);
  }
  .award-badge {
    position: absolute;
    left: 957px;
    top: 0;
    width: 142px;
    height: 272px;
  }
  .award-badge svg {
    display: block;
  }
</style>
</head>
<body>
  <main class="canvas">
    <section class="header-banner">
      <div class="header-photo" role="img" aria-label="Photo of business people at a meeting table shaking hands, with a potted plant, coffee cups and a pen holder"></div>

      <div class="brand-panel">
        <svg width="355" height="67" viewBox="0 0 355 67" aria-hidden="true">
          <polygon points="0,0 355,0 355,67 62,67" fill="var(--panel)" opacity="0.96"/>
        </svg>
        <p class="brand-name">MORVADA</p>
        <p class="brand-tagline">Management Consulting</p>
      </div>

      <div class="award-badge" role="img" aria-label="Consulting award listing badge">
        <svg width="142" height="272" viewBox="0 0 142 272">
          <defs>
            <linearGradient id="badgeGold" x1="0" y1="0" x2="1" y2="1">
              <stop offset="0" stop-color="var(--gold-light)"/>
              <stop offset="0.5" stop-color="var(--gold-mid)"/>
              <stop offset="1" stop-color="var(--gold-dark)"/>
            </linearGradient>
          </defs>
          <rect x="0.5" y="0.5" width="141" height="271" fill="var(--badge-white)" stroke="var(--badge-edge)" stroke-width="1"/>
          <rect x="0" y="0" width="142" height="141" fill="url(#badgeGold)"/>
        </svg>
      </div>
    </section>
  </main>
</body>
</html>
```